Corvath Staffing Solutions - Magazine Ad

Local magazine ad for Corvath Staffing Solutions.
We are targeting local businesses, namely hospitality clients in the local Laguna Beach, CA area. This is an upscale, rather fancy, area so the target audience will be of a more professional sense. We want this advertisement to stand out from the rest. Feel free to use beach and other Laguna Beach, CA pics.
We want to provide the following contact info, clearly visible to direct traffic.
Contact info:
Mina Thorley
mthorley@Corvath.com
949-382-4066
Should include the text:
"Servicing:
- Professional
- Clerical
- Hospitality
- FInancial
- Highly Skilled Industrial"
Please include: www.Corvath.com
This will be a full page ad.

```html
<!DOCTYPE html>
<html lang="en">
<head>
<meta charset="utf-8">
<title>Corvath Staffing Solutions – Magazine Ad</title>
<link href="https://fonts.googleapis.com/css2?family=Arimo:wght@400;700&display=swap" rel="stylesheet">
<style>
  :root {
    --sky-top: #f2b45a;
    --sky-mid: #e9a860;
    --shore: #3a2a24;
    --sand: #2a211e;
    --red: #e0262b;
    --orange-top: #e84a2c;
    --orange-bottom: #f6a225;
    --blue: #1f86dc;
    --blue-deep: #1a5fa8;
    --white: #ffffff;
  }
  html, body {
    margin: 0;
    padding: 0;
    overflow: hidden;
    background: #ffffff;
  }
  .ad {
    position: relative;
    width: 927px;
    height: 1200px;
    overflow: hidden;
    font-family: "Arimo", Arial, sans-serif;
  }
  .ad__photo {
    position: absolute;
    inset: 0;
    background: linear-gradient(180deg,
      #d9885a 0%,
      var(--sky-top) 38%,
      #f4cf86 50%,
      var(--sky-mid) 58%,
      #5a4034 66%,
      var(--shore) 72%,
      var(--sand) 100%);
  }
  .ad__shapes {
    position: absolute;
    inset: 0;
  }
  .services {
    position: absolute;
    left: 92px;
    top: 90px;
    width: 238px;
  }
  .services__label {
    display: block;
    width: 234px;
    height: 28px;
    background: var(--white);
    color: var(--red);
    font-weight: 700;
    font-size: 24px;
    line-height: 29px;
    padding-left: 7px;
    box-sizing: border-box;
    margin: 0 0 20px 0;
  }
  .services__list {
    list-style: none;
    margin: 0;
    padding: 0;
  }
  .services__item {
    color: var(--white);
    font-weight: 700;
    font-size: 29px;
    line-height: 26px;
    padding-bottom: 4px;
    border-bottom: 1.5px solid var(--white);
    margin-bottom: 17px;
    white-space: nowrap;
  }
  .services__item--double { line-height: 27px; }
  .brand {
    position: absolute;
    left: 88px;
    top: 996px;
    display: flex;
    align-items: center;
    gap: 10px;
    color: var(--white);
    font-weight: 700;
    font-size: 20px;
    line-height: 24px;
    white-space: nowrap;
  }
  .brand__mark {
    width: 16px;
    height: 16px;
    background: var(--white);
  }
  .contact {
    position: absolute;
    left: 552px;
    width: 320px;
    top: 986px;
    text-align: center;
    color: var(--white);
    font-style: normal;
  }
  .contact__name {
    font-weight: 700;
    font-size: 37px;
    line-height: 44px;
    margin: 0;
  }
  .contact__line {
    font-size: 27px;
    line-height: 34px;
    margin: 0;
  }
  .contact__web {
    font-weight: 700;
    font-size: 23px;
    margin: 30px 0 0;
  }
</style>
</head>
<body>
<main class="ad">
  <div class="ad__photo" role="img" aria-label="Sunset photograph of Laguna Beach with palm trees on a cliff and people walking on the sand"></div>

  <svg class="ad__shapes" width="927" height="1200" viewBox="0 0 927 1200" aria-hidden="true">
    <defs>
      <linearGradient id="orangeFade" x1="0" y1="0" x2="0" y2="1">
        <stop offset="0" stop-color="var(--orange-top)"/>
        <stop offset="1" stop-color="var(--orange-bottom)"/>
      </linearGradient>
    </defs>
    <polygon points="0,0 344,0 552,204 184,572 0,392" fill="url(#orangeFade)" opacity="0.93"/>
    <polygon points="0,500 184,572 130,620 0,620" fill="#f08a2a" opacity="0.25"/>
    <polygon points="344,0 752,0 552,204" fill="var(--red)" opacity="0.95"/>
    <polygon points="552,204 752,0 927,0 927,96 676,328" fill="#ffffff" opacity="0.22"/>
    <polygon points="600,260 927,96 927,200 676,328" fill="#ffffff" opacity="0.12"/>
    <polygon points="264,1200 712,668 927,880 927,1200" fill="var(--blue-deep)" opacity="0.4"/>
    <polygon points="384,1200 718,832 927,1040 927,1200" fill="var(--blue)" opacity="0.65"/>
    <polygon points="72,1200 186,1076 312,1200" fill="var(--blue)" opacity="0.45"/>
  </svg>

  <section class="services">
    <span class="services__label">SERVICING:</span>
    <ul class="services__list">
      <li class="services__item">PROFESSIONAL</li>
      <li class="services__item">CLERICAL</li>
      <li class="services__item">HOSPITALITY</li>
      <li class="services__item">FINANCIAL</li>
      <li class="services__item services__item--double">HIGHLY SKILLED<br>INDUSTRIAL</li>
    </ul>
  </section>

  <div class="brand">
    <span class="brand__mark"></span>
    <span class="brand__name">Corvath Staffing Solutions</span>
  </div>

  <address class="contact">
    <p class="contact__name">Mina Thorley</p>
    <p class="contact__line">mthorley@Corvath.com</p>
    <p class="contact__line">949-382-4066</p>
    <p class="contact__web">www.Corvath.com</p>
  </address>
</main>
</body>
</html>
```